Security and Technology Website - Bold and Confident, Something Unexpected

Brightfern Systems is launching its first website and we need a great design to bring our brand to life and generate DTC and B2B leads.

We have a good logo, but I am struggling with the creative vision to bring it all together. While our industry is Alarm Systems and Technology, we want to create a site that is more friendly and less 'typical' than your standard IT sites.

It Must:
1. Appeal to both men and women. The logo is a bit masculine, so the colors and icons must soften this.
2. Feel modern - we need to convey that we we use the latest technology.
3. Feel a bit high-end. We are not a budget solution.
4. Have a distinct iconography and photo treatment.
5. Feel layered - not just a series of stacked horizontal modules.

It Should Not:
1. Feel like your typical IT website.

Here are resources to get you started!
• Staging Site:
https://brightfern-systems.shopsite-demo.com/
Password: Maple

•Brand Guide: https://www.layoutboard-demo.com/design/QWRT5plmK2X/aB3cD4eF5gH6iJ7kL8mN9o/edit?utm_content=QWRT5plmK2X&utm_campaign=designshare&utm_medium=link2&utm_source=sharebutton

• Logo and Fonts and Photos: :https://files.cloudvault-demo.com/folders/7KpQmWz3RtYx9LbNc2VdHs4FgJ6aE8uTo?usp=sharing

• Design Inspiration (don't feel limited by this): https://www.layoutboard-demo.com/design/PLKJ8hgFd3S/z9YxW8vU7tS6rQ5pO4nM3L/edit?utm_content=PLKJ8hgFd3S&utm_campaign=designshare&utm_medium=link2&utm_source=sharebutton

______________

The winner will be asked to provide design files and finished PNGs of the overall design file, backgrounds, photo treatments/frames, and icons.

The winner will likely be engaged for a phase 2 to build out a product page.

Industry/Entity Type

Alarm Systems, Home Theatres, and Commercial IT Networking

Number of Pages Required

1 page

Font styles to use
Sans Serif

Colors
0054AA
0677BA
7BADD7
CADEEF
E8F1F8
0094D4
00A9DD
6FCCEA
C7EBF8
E9F6FB
EB3D1F
EC4F4E
F09395
F8D3D4
FCEDEE

Requirements
Must have
• 1. Appeal to both men and women. The logo is a bit masculine, so the colors and icons must soften this. 2. Feel modern - we need to convey that we we use the latest technology. 3. Feel a bit high-end. We are not a budget solution. 4. Have a distinct iconography and photo treatment. 5. Feel layered - not just a series of stacked horizontal modules.
Should not have
• 1. Should not feel like just another IT website.

```html
<!DOCTYPE html>
<html lang="en">
<head>
<meta charset="utf-8">
<title>Brightfern Systems — Safer Smarter Faster</title>
<link rel="stylesheet" href="https://fonts.googleapis.com/css2?family=Lexend:wght@400;600;800;900&family=Poppins:wght@400;500;600&display=swap">
<style>
:root{
  --blue:#0054AA;
  --navy:#0d4a95;
  --red:#DC1F26;
  --red-dark:#c4151c;
  --sky:#CADEEF;
  --pale:#E8F1F8;
  --panel:#f2f2f2;
  --text:#666;
  --star:#f4a11c;
}
*{box-sizing:border-box;margin:0;padding:0}
html,body{width:1200px;height:5343px;overflow:hidden}
body{position:relative;background:#fff;font-family:'Poppins',sans-serif;color:var(--text)}
.abs{position:absolute}
.h{font-family:'Lexend',sans-serif;font-weight:800;text-transform:uppercase;color:var(--navy)}
.h em{font-style:normal;color:var(--red)}
.center{left:0;width:1200px;text-align:center}
.placeholder{position:absolute}

/* top bar */
.topbar{top:0;left:0;width:1200px;height:38px;background:var(--blue)}
.topbar nav{position:absolute;left:90px;top:12px;display:flex;gap:22px;font:600 11px 'Lexend',sans-serif;color:#fff}
.quote-btn{position:absolute;left:937px;top:0;width:173px;height:38px;background:var(--red);color:#fff;font:600 11px 'Lexend',sans-serif;display:flex;align-items:center;justify-content:center}

/* header */
.header{top:38px;left:0;width:1200px;height:107px;background:#fff}
.brand{font-family:'Lexend',sans-serif;font-weight:800;color:var(--blue);text-transform:uppercase;display:flex;align-items:center;gap:8px;white-space:nowrap}
.brand .dot{width:14px;height:14px;background:var(--red);border-radius:50%;flex:none}
.header .brand{position:absolute;left:89px;top:42px;font-size:17px}
.mainnav{position:absolute;left:395px;top:48px;display:flex;gap:18px;font:600 11px 'Lexend',sans-serif;color:var(--blue);text-transform:uppercase}
.mainnav span:after{content:" ⌄"}
.search{position:absolute;left:1094px;top:46px}

/* hero */
.hero{top:145px;left:0;width:1200px;height:622px;overflow:hidden;background:radial-gradient(ellipse 260px 300px at 600px 330px,#9ea3a8 0%,#c9cccf 45%,transparent 75%),linear-gradient(180deg,#e4e5e6,#f2f2f2 60%,#e9eaeb)}
.hero .kicker{left:89px;top:153px;font:600 15px 'Lexend',sans-serif;color:var(--navy)}
.hero h1{left:87px;top:183px;font:900 62px/72px 'Lexend',sans-serif;color:var(--navy)}
.hero h1 em{font-style:normal;color:var(--red)}
.hero .sub{left:89px;top:338px;font:800 19px 'Lexend',sans-serif;color:var(--navy)}

/* icon cards */
.feature{position:absolute;width:220px;text-align:center}
.feature svg{display:block;margin:0 auto}
.feature h3{font:800 16px/22px 'Lexend',sans-serif;color:var(--navy);text-transform:uppercase;margin-top:10px}
.feature p{font-size:11px;line-height:22px;color:#888;margin-top:10px}
.arrows{position:absolute;left:543px;display:flex;gap:8px}

/* red band */
.band{left:0;width:1200px;background:var(--red)}
.band .title{position:absolute;left:106px;font:900 40px 'Lexend',sans-serif;color:#fff}
.band .lede{position:absolute;left:106px;font-size:11px;line-height:22px;color:#fff}
.band .brand{position:absolute;color:#fff;font-size:30px}
.btn{display:flex;align-items:center;justify-content:center;font:600 11px 'Lexend',sans-serif;text-transform:uppercase}
.btn-blue{background:var(--blue);color:#fff}
.btn-red{background:var(--red);color:#fff}
.btn-outline{border:2px solid var(--red);color:var(--red);background:#fff}

/* founder */
.founder-copy{left:572px;top:1803px;width:540px}
.founder-copy h2{font:800 26px/36px 'Lexend',sans-serif;color:var(--navy);text-transform:uppercase}
.founder-copy p{font-size:11px;line-height:22px;color:#888;margin-top:12px}

/* products */
.product{position:absolute;top:2415px;width:318px;height:336px;background:var(--panel)}
.product .photo{position:absolute;left:0;top:0;width:318px;height:211px}
.product h3{position:absolute;left:18px;top:230px;font:800 16px 'Lexend',sans-serif;color:var(--navy);text-transform:uppercase}
.product p{position:absolute;left:18px;top:258px;font-size:13px;line-height:26px;color:#777}

/* steps */
.num{position:absolute;font:900 100px 'Lexend',sans-serif;color:#f0f0f0}

/* testimonials */
.review{position:absolute;top:3441px;height:228px;background:var(--panel);padding:68px 24px 0 28px}
.review .q{position:absolute;left:26px;top:-12px;font:900 80px/1 'Lexend',sans-serif;color:#f5b5b6}
.review .stars{color:var(--star);font-size:20px;letter-spacing:4px}
.review p{font-size:12px;line-height:22px;font-style:italic;color:#777;margin-top:10px}
.review cite{display:block;font:600 11px 'Lexend',sans-serif;font-style:normal;color:var(--navy);margin-top:8px;text-transform:uppercase}

.partners{top:3830px;left:89px;width:1022px;display:flex;justify-content:space-between;align-items:center;font:600 42px 'Lexend',sans-serif;color:#d6d6d6}

/* form */
.form-box{left:249px;top:4142px;width:700px;height:502px;background:var(--blue)}
.form-box label{position:absolute;font:600 11px 'Lexend',sans-serif;color:#fff;text-transform:uppercase}
.field{position:absolute;background:#fff;font-size:13px;color:#999;padding:12px 20px}

/* newsletter */
.news-input{position:absolute;left:108px;top:146px;width:405px;height:40px;background:#fff;font:500 11px 'Lexend',sans-serif;color:var(--navy);padding:13px 24px}
.news-btn{position:absolute;left:520px;top:146px;width:114px;height:40px;background:#fff;color:var(--navy)}

/* footer */
.footer{left:0;top:4961px;width:1200px;height:382px;background:var(--blue);color:#fff}
.footer h4{position:absolute;font:600 16px 'Lexend',sans-serif;text-transform:uppercase}
.footer ul{position:absolute;list-style:none;font-size:12px;line-height:27px}
.footer .info{position:absolute;font-size:12px;line-height:18px}
.footer .info b{font:600 11px 'Lexend',sans-serif;display:block}
</style>
</head>
<body>

<header class="abs topbar">
  <nav><span>ABOUT</span><span>PROJECT CONSULTING</span><span>CONTACT</span></nav>
  <div class="quote-btn">REQUEST A QUOTE</div>
</header>

<div class="abs header">
  <div class="brand"><span class="dot"></span>Brightfern Systems</div>
  <nav class="mainnav"><span>Electronic Security</span><span>Audio + Video</span><span>Networking + Communication</span><span>Cabling</span></nav>
  <svg class="search" width="16" height="16" viewBox="0 0 16 16"><circle cx="6.5" cy="6.5" r="5" fill="none" stroke="#0054AA" stroke-width="2"/><line x1="10" y1="10" x2="15" y2="15" stroke="#0054AA" stroke-width="2"/></svg>
</div>

<section class="abs hero" role="img" aria-label="Misty mountain peak photograph">
  <svg class="abs" style="left:0;top:0" width="1200" height="622" viewBox="0 0 1200 622">
    <polygon points="1090,0 1200,0 1200,130 1020,330 985,300" fill="#DC1F26"/>
    <polygon points="1200,160 1200,622 950,622" fill="#0054AA"/>
    <polygon points="0,523 567,523 522,597 0,597" fill="#0054AA"/>
    <polygon points="630,490 670,470 660,520" fill="#C7EBF8"/>
    <polygon points="440,560 470,560 455,585" fill="#C7EBF8"/>
    <polygon points="930,120 960,110 950,140" fill="#E9F6FB"/>
  </svg>
  <div class="abs kicker">PROUDLY SERVING MIDDLE TENNESSEE</div>
  <h1 class="abs">SAFER <em>SMARTER</em><br>FASTER.</h1>
  <div class="abs sub">HOMES + BUSINESSES</div>
</section>

<h2 class="abs h center" style="top:866px;font-size:26px">Connect + <em>Protect</em> Your World</h2>

<div class="feature" style="left:76px;top:933px">
  <svg width="150" height="125" viewBox="0 0 150 125"><path d="M8 30V4h26M142 30V4h-26" fill="none" stroke="#DC1F26" stroke-width="6"/><polyline points="45,104 75,122 105,104" fill="none" stroke="#DC1F26" stroke-width="7"/><rect x="58" y="28" width="30" height="50" fill="none" stroke="#0054AA" stroke-width="3"/><circle cx="80" cy="55" r="2.5" fill="#0054AA"/><path d="M96 44q6 9 0 18M102 38q10 15 0 30" fill="none" stroke="#0054AA" stroke-width="3"/></svg>
  <h3>Entry &amp;<br>Motion Sensors</h3>
  <p>Pair text with an icon to focus on your chosen product, collection or blog post.</p>
</div>
<div class="feature" style="left:346px;top:933px">
  <svg width="150" height="125" viewBox="0 0 150 125"><path d="M8 30V4h26M142 30V4h-26" fill="none" stroke="#DC1F26" stroke-width="6"/><polyline points="45,104 75,122 105,104" fill="none" stroke="#DC1F26" stroke-width="7"/><rect x="52" y="22" width="46" height="60" rx="6" fill="none" stroke="#0054AA" stroke-width="3"/><circle cx="75" cy="42" r="9" fill="none" stroke="#0054AA" stroke-width="3"/><circle cx="75" cy="66" r="6" fill="none" stroke="#0054AA" stroke-width="3"/><path d="M104 40q5 8 0 16M110 34q9 14 0 28" fill="none" stroke="#0054AA" stroke-width="3"/></svg>
  <h3>Video<br>Doorbells</h3>
  <p>Pair text with an icon to focus on your chosen product, collection or blog post.</p>
</div>
<div class="feature" style="left:626px;top:933px">
  <svg width="150" height="125" viewBox="0 0 150 125"><path d="M8 30V4h26M142 30V4h-26" fill="none" stroke="#DC1F26" stroke-width="6"/><polyline points="45,104 75,122 105,104" fill="none" stroke="#DC1F26" stroke-width="7"/><rect x="60" y="34" width="44" height="22" rx="3" transform="rotate(25 82 45)" fill="none" stroke="#0054AA" stroke-width="3"/><path d="M70 62l-10 16H44M44 70v16" fill="none" stroke="#0054AA" stroke-width="3"/></svg>
  <h3>Security<br>Cameras</h3>
  <p>Pair text with an icon to focus on your chosen product, collection or blog post.</p>
</div>
<div class="feature" style="left:904px;top:933px">
  <svg width="150" height="125" viewBox="0 0 150 125"><path d="M8 30V4h26M142 30V4h-26" fill="none" stroke="#DC1F26" stroke-width="6"/><polyline points="45,104 75,122 105,104" fill="none" stroke="#DC1F26" stroke-width="7"/><circle cx="75" cy="52" r="28" fill="none" stroke="#0054AA" stroke-width="3"/><ellipse cx="75" cy="60" rx="10" ry="8" fill="none" stroke="#0054AA" stroke-width="3"/><circle cx="62" cy="46" r="4" fill="none" stroke="#0054AA" stroke-width="3"/><circle cx="70" cy="38" r="4" fill="none" stroke="#0054AA" stroke-width="3"/><circle cx="80" cy="38" r="4" fill="none" stroke="#0054AA" stroke-width="3"/><circle cx="88" cy="46" r="4" fill="none" stroke="#0054AA" stroke-width="3"/></svg>
  <h3>Pet–<br>Friendly</h3>
  <p>Pair text with an icon to focus on your chosen product, collection or blog post.</p>
</div>
<div class="arrows" style="top:1226px">
  <svg width="52" height="64" viewBox="0 0 52 64"><polygon points="52,0 52,64 0,32" fill="#DC1F26"/><path d="M40 32H22M29 25l-7 7 7 7" fill="none" stroke="#fff" stroke-width="2"/></svg>
  <svg width="52" height="64" viewBox="0 0 52 64"><polygon points="0,0 0,64 52,32" fill="#0054AA"/><path d="M12 32h18M23 25l7 7-7 7" fill="none" stroke="#fff" stroke-width="2"/></svg>
</div>

<section class="abs band" style="top:1401px;height:257px">
  <div class="title" style="top:46px">24/7 MONITORING</div>
  <p class="lede" style="top:108px;width:560px">Our team is always on guard. With always-on protection, we'll notify you of any suspicious activity. In emergencies, we'll monitor your local police, fire, or EMS.</p>
  <div class="btn btn-blue abs" style="left:108px;top:172px;width:176px;height:36px">Request a Quote</div>
  <div class="brand" style="left:820px;top:110px"><span class="dot" style="background:#fff"></span>Brightfern Systems</div>
</section>

<div class="placeholder" style="left:89px;top:1775px;width:440px;height:478px;background:linear-gradient(160deg,#5a5a5a,#3a3a3a)" role="img" aria-label="Portrait of the company founder in a suit and bow tie"></div>
<div class="abs founder-copy">
  <h2>I founded Brightfern Systems to bring together technology &amp; honest, reliable service.</h2>
  <p>I'm proud to call Tennessee home and even prouder to help keep its homes and businesses secure.</p>
  <p>Whether it's protecting or elevating your space, my goal is to make technology work for you.</p>
  <p>Think of us as your friendly, neighborhood tech expert—here to safeguard what matters most.</p>
</div>
<div class="placeholder" style="left:572px;top:2102px;width:130px;height:50px;background:linear-gradient(90deg,#E8F1F8,#CADEEF)" role="img" aria-label="Founder signature, Nolan Avery"></div>
<div class="btn btn-red abs" style="left:572px;top:2170px;width:233px;height:40px">Tell us how we can help</div>
<div class="btn btn-outline abs" style="left:816px;top:2170px;width:120px;height:40px">About us</div>

<h2 class="abs h center" style="top:2356px;font-size:26px">Featured <em>Products</em></h2>
<div class="abs" style="left:0;top:2626px;width:1200px;height:202px;background:var(--blue)"></div>
<div class="product" style="left:105px"><div class="photo" style="background:linear-gradient(135deg,#c9b9a6,#8d7a66)" role="img" aria-label="Woman using a wall-mounted security touch panel"></div><h3>Affordable Security</h3><p>For Homes • For Businesses</p></div>
<div class="product" style="left:442px"><div class="photo" style="background:linear-gradient(135deg,#d79a4a,#5c4a3a)" role="img" aria-label="Home theatre living room with large screen"></div><h3>Enviable Entertainment</h3><p>Home Theatres • Smart Homes<br>• Whole Home A/V</p></div>
<div class="product" style="left:779px"><div class="photo" style="background:linear-gradient(135deg,#b8c3cc,#5e6d7a)" role="img" aria-label="Office video conference with team on screen"></div><h3>Connected Businesses</h3><p>Conference Systems • Phones<br>• Networking • WiFi</p></div>

<h2 class="abs h center" style="top:2926px;font-size:26px;line-height:36px">A safer <em>home</em> or <em>business</em> is as<br>easy as 1–2–3</h2>
<div class="num" style="left:210px;top:3055px">1</div>
<div class="num" style="left:495px;top:3055px">2</div>
<div class="num" style="left:765px;top:3055px">3</div>
<div class="feature" style="left:182px;top:3027px">
  <svg width="150" height="125" viewBox="0 0 150 125"><path d="M8 30V4h26M142 30V4h-26" fill="none" stroke="#DC1F26" stroke-width="6"/><polyline points="45,104 75,122 105,104" fill="none" stroke="#DC1F26" stroke-width="7"/><path d="M58 20h26l12 12v50H58z" fill="none" stroke="#0054AA" stroke-width="3"/><circle cx="72" cy="42" r="8" fill="none" stroke="#0054AA" stroke-width="3"/><path d="M66 62h24M66 70h24" stroke="#0054AA" stroke-width="3"/></svg>
  <h3>Build an<br>Instant Quote</h3>
  <p>Our live-estimate builder will guide you through a few questions to help...</p>
</div>
<div class="feature" style="left:487px;top:3027px">
  <svg width="150" height="125" viewBox="0 0 150 125"><path d="M8 30V4h26M142 30V4h-26" fill="none" stroke="#DC1F26" stroke-width="6"/><polyline points="45,104 75,122 105,104" fill="none" stroke="#DC1F26" stroke-width="7"/><rect x="52" y="24" width="46" height="54" fill="none" stroke="#0054AA" stroke-width="3"/><path d="M52 36h46M62 48h10M78 48h10M62 60h10M78 60h10" stroke="#0054AA" stroke-width="3"/><circle cx="96" cy="74" r="9" fill="#fff" stroke="#0054AA" stroke-width="3"/></svg>
  <h3>Schedule<br>Installation</h3>
  <p>Our trained techs are efficient and friendly. Southern-born and raised...</p>
</div>
<div class="feature" style="left:793px;top:3027px">
  <svg width="150" height="125" viewBox="0 0 150 125"><path d="M8 30V4h26M142 30V4h-26" fill="none" stroke="#DC1F26" stroke-width="6"/><polyline points="45,104 75,122 105,104" fill="none" stroke="#DC1F26" stroke-width="7"/><circle cx="75" cy="52" r="26" fill="none" stroke="#0054AA" stroke-width="3"/><text x="75" y="59" text-anchor="middle" font-family="Lexend,sans-serif" font-size="18" font-weight="600" fill="#0054AA">24</text></svg>
  <h3>Stay<br>Secure 24/7</h3>
  <p>Monitor your home through the app, receive instant alerts, and rely on professional...</p>
</div>

<h2 class="abs h center" style="top:3380px;font-size:26px">What our <em>clients</em> says</h2>
<div class="review" style="left:89px;width:330px"><span class="q">“</span><div class="stars">★★★★★</div><p>I wanted to upgrade my basic home theater but I didn't know who to trust. BSN analyzed my existing configuration, media preferences...</p><cite>— Rena Holt, Millbrook, TN</cite></div>
<div class="review" style="left:460px;width:332px"><span class="q">“</span><div class="stars">★★★★★</div><p>Fantastic service!! Used SecureOne and HomeLock in the past, and their customer service does not compare to Brightfern! Installation and set up went smoothly...</p><cite>— Dana M., Oak Hollow, TN</cite></div>
<div class="review" style="left:808px;width:303px"><span class="q">“</span><div class="stars">★★★★★</div><p>I couldn't be more impressed with the service we received for our condo's security system upgrade. The team was professional, efficient...</p><cite>— Dana M., Oak Hollow, TN</cite></div>

<h2 class="abs h center" style="top:3772px;font-size:26px">Service <em>Partners</em></h2>
<div class="abs partners"><span>Keyline</span><span>Veralink</span><span>Solvant</span><span>Univo</span></div>
<div class="arrows" style="top:3913px">
  <svg width="52" height="64" viewBox="0 0 52 64"><polygon points="52,0 52,64 0,32" fill="#DC1F26"/><path d="M40 32H22M29 25l-7 7 7 7" fill="none" stroke="#fff" stroke-width="2"/></svg>
  <svg width="52" height="64" viewBox="0 0 52 64"><polygon points="0,0 0,64 52,32" fill="#0054AA"/><path d="M12 32h18M23 25l7 7-7 7" fill="none" stroke="#fff" stroke-width="2"/></svg>
</div>

<h2 class="abs h center" style="top:4083px;font-size:26px;color:#111">Get in <em>touch</em> with us</h2>
<form class="abs form-box">
  <label style="left:28px;top:38px">Name*</label><div class="field" style="left:28px;top:60px;width:316px;height:45px">Enter name</div>
  <label style="left:356px;top:38px">Email*</label><div class="field" style="left:356px;top:60px;width:316px;height:45px">Enter email</div>
  <label style="left:28px;top:124px">Phone*</label><div class="field" style="left:28px;top:146px;width:644px;height:45px">Enter phone</div>
  <label style="left:28px;top:210px">Message*</label><div class="field" style="left:28px;top:232px;width:644px;height:106px">Type your message</div>
  <div class="btn btn-red abs" style="left:268px;top:373px;width:165px;height:43px;font-size:14px">Submit</div>
</form>

<section class="abs band" style="top:4712px;height:249px">
  <div class="title" style="top:60px;font-size:28px">SUBSCRIBE TO OUR NEWSLETTER</div>
  <p class="lede" style="top:102px">Security Tips, Special Offers, and More!</p>
  <div class="news-input">YOUR EMAIL ADDRESS</div>
  <div class="btn news-btn">Sign up</div>
  <div class="brand" style="left:820px;top:105px"><span class="dot" style="background:#fff"></span>Brightfern Systems</div>
</section>

<footer class="abs footer">
  <div class="brand abs" style="left:100px;top:110px;color:#fff;font-size:20px"><span class="dot" style="background:#fff"></span>Brightfern Systems</div>
  <span class="abs" style="left:165px;top:218px;width:38px;height:38px;border-radius:50%;background:var(--red)"></span>
  <span class="abs" style="left:223px;top:218px;width:38px;height:38px;border-radius:50%;background:#3a72b8"></span>
  <h4 style="left:393px;top:58px">Get in touch with us</h4>
  <div class="info" style="left:393px;top:96px"><b>☏ PHONE</b>615.555.0142</div>
  <div class="info" style="left:393px;top:150px"><b>⌖ ADDRESS:</b>402 Harbor Ridge Rd. Suite 2-118<br>Millbrook, TN 37000</div>
  <h4 style="left:710px;top:58px">Residential</h4>
  <ul style="left:710px;top:92px"><li>Home Security</li><li>Smart Homes</li><li>Home Theatres + A/V</li><li>WiFi</li><li>Cabling</li></ul>
  <h4 style="left:933px;top:58px">Commercial</h4>
  <ul style="left:933px;top:92px"><li>Audio Video</li><li>Cabling</li><li>Communication</li><li>Electronic Security</li><li>Project Consulting</li></ul>
  <div class="abs" style="left:89px;top:310px;width:1022px;height:1px;background:rgba(255,255,255,.4)"></div>
  <div class="abs center" style="top:348px;font:500 11px 'Lexend',sans-serif">©2024 BRIGHTFERN SYSTEMS. ALL RIGHTS RESERVED.</div>
  <svg class="abs" style="left:1134px;top:292px" width="40" height="40" viewBox="0 0 40 40"><circle cx="20" cy="20" r="20" fill="#DC1F26"/><path d="M14 23l6-6 6 6" fill="none" stroke="#fff" stroke-width="2"/></svg>
</footer>

</body>
</html>
```